ARRIVAL OF MARTIN THE OLD COUSIN

Hello everyone !

Our establishment, on 57 in CAMBRAI will have the pleasure of welcoming MARTIN LE VIEUX COUSIN, idol of young people, on Friday May 13, 2022, from 7:00 p.m.
On the program, photo session and dedications.
A VIP table will be offered to share the meal with him!
Only 12 places available at his table!
The brasserie will offer a barbecue for the occasion.
Admission with meal: €15
Seating at the VIP table: €65 (starter - main course - dessert); Champagne.
Happy HOURS on beers and cocktails!
Reservation strongly recommended.

I remain at your disposal ;

To your ideas!

```html
<!DOCTYPE html>
<html lang="fr">
<head>
<meta charset="utf-8">
<title>Arrivée de Martin le Vieux Cousin</title>
<link rel="stylesheet" href="https://fonts.googleapis.com/css2?family=Montserrat:wght@400;500;600;700;800;900&display=swap">
<style>
  :root {
    --red: #d71f27;
    --red-dark: #a6232b;
    --ink: #1a0a14;
    --gold: #c98a2c;
    --gold-light: #dca23a;
    --white: #ffffff;
    --navy: #1b2360;
    --navy-deep: #121a4a;
    --teal: #0b86b4;
  }
  * { margin: 0; padding: 0; box-sizing: border-box; }
  html, body { width: 927px; height: 1200px; overflow: hidden; background: var(--white); }
  .poster {
    position: relative; width: 927px; height: 1200px; overflow: hidden;
    background: var(--white);
    font-family: "Montserrat", Arial, sans-serif;
    color: var(--ink);
  }
  .poster > * { position: absolute; }

  /* headline */
  .headline-kicker { left: 157px; top: 22px; font-size: 52px; font-weight: 600; letter-spacing: 1px; line-height: 1; }
  .headline-bar { left: 0; top: 85px; width: 40px; height: 93px; background: var(--red); }
  .headline-name { left: 64px; top: 74px; font-size: 122px; font-weight: 800; color: var(--red); line-height: 1; letter-spacing: -1px; }
  .headline-title {
    left: 622px; top: 87px; width: 305px; height: 91px; background: var(--red);
    color: var(--white); font-size: 34px; font-weight: 500; line-height: 40px;
    padding: 8px 0 0 17px; letter-spacing: 1px;
  }

  /* venue */
  .venue-mark { left: 0; top: 222px; width: 927px; display: flex; justify-content: center; align-items: center; gap: 18px; }
  .venue-dot { width: 44px; height: 44px; border-radius: 50%; border: 3px solid var(--gold); }
  .venue-name { font-size: 46px; font-weight: 500; color: var(--gold); letter-spacing: 1px; line-height: 1; }
  .venue-tag { top: 291px; font-size: 10px; font-weight: 600; letter-spacing: .3px; }
  .venue-tag--left { left: 289px; }
  .venue-tag--right { left: 590px; }

  /* event */
  .event-place { left: 440px; width: 465px; top: 360px; text-align: center; font-size: 24px; font-weight: 700; }
  .event-welcome { left: 440px; width: 470px; top: 394px; text-align: center; font-size: 48px; font-weight: 800; color: var(--red-dark); letter-spacing: 1px; }
  .event-when { top: 472px; font-size: 22px; font-weight: 700; line-height: 31px; }
  .event-when span { display: block; color: var(--red); }
  .event-when--date { left: 483px; }
  .event-when--time { left: 681px; }
  .event-divider { left: 663px; top: 469px; width: 2px; height: 69px; background: var(--ink); }
  .event-program { left: 410px; width: 450px; top: 559px; text-align: center; font-size: 22px; font-weight: 700; line-height: 31px; }
  .event-program span { display: block; color: var(--red-dark); }

  /* backgrounds */
  .portrait {
    left: 0; top: 310px; width: 520px; height: 890px;
    background: linear-gradient(170deg, rgba(255,255,255,0) 0%, #e6a7c0 12%, #c25c8e 35%, #2a1430 55%, #6b1f4a 70%, #3b2a86 85%, #2a2f7a 100%);
  }
  .backdrop {
    left: 430px; top: 852px; width: 497px; height: 348px;
    background: linear-gradient(135deg, var(--navy) 0%, #1d3b85 45%, var(--teal) 100%);
  }

  /* vip */
  .vip {
    left: 477px; top: 634px; width: 348px; height: 342px;
    background: linear-gradient(160deg, #3a2a6e 0%, var(--navy-deep) 45%, #1d3a7a 100%);
    box-shadow: 6px 6px 10px rgba(0,0,0,.35);
  }
  .vip-frame { position: absolute; left: 18px; top: 17px; width: 314px; height: 309px; border: 2px solid rgba(120,170,220,.6); }
  .vip-content { position: absolute; left: 0; top: 0; width: 100%; text-align: center; color: var(--white); }
  .vip-price { margin-top: 22px; font-size: 48px; font-weight: 700; line-height: 1; padding-right: 16px; }
  .vip-label { font-size: 38px; font-weight: 800; color: var(--gold); line-height: 1.05; }
  .vip-offer { margin-top: 6px; font-size: 19px; font-weight: 700; line-height: 27.5px; letter-spacing: .5px; }
  .vip-menu { margin-top: 34px; font-size: 11px; font-weight: 400; letter-spacing: .2px; }
  .vip-seats { margin-top: 12px; font-size: 17px; font-weight: 700; color: var(--gold-light); line-height: 21px; }
  .vip-seats span { display: block; font-size: 14px; }

  /* extras */
  .extras-bbq { left: 460px; width: 395px; top: 982px; text-align: center; color: var(--white); font-size: 21px; font-weight: 700; line-height: 29px; }
  .extras-price { left: 416px; top: 1055px; color: var(--white); font-size: 60px; font-weight: 700; line-height: 1; letter-spacing: -2px; }
  .extras-note { color: var(--white); font-size: 17px; font-weight: 500; line-height: 24px; }
  .extras-note--admission { left: 531px; top: 1063px; }
  .extras-note--happy { left: 733px; top: 1061px; }
  .extras-divider { left: 658px; top: 1056px; width: 2px; height: 56px; background: var(--white); }
  .extras-icon { left: 674px; top: 1060px; width: 48px; height: 52px; }

  .footer-band-left { left: 30px; top: 1128px; width: 545px; height: 32px; background: linear-gradient(90deg, #3b3416, #241b3a); }
  .footer-band-right {
    left: 566px; top: 1128px; width: 335px; height: 32px; background: #152048;
    clip-path: polygon(0 0, 100% 0, 100% 100%, 10% 100%);
  }
  .footer-note { right: 27px; top: 1134px; color: var(--white); font-size: 15px; font-weight: 500; }
</style>
</head>
<body>
<div class="poster">
  <div class="portrait" role="img" aria-label="Portrait photo de Martin le Vieux Cousin, bras croisés, en chemise noire, éclairage rose et violet"></div>
  <div class="backdrop"></div>

  <div class="headline-kicker">ARRIVÉE DE</div>
  <div class="headline-bar"></div>
  <div class="headline-name">MARTIN</div>
  <div class="headline-title">LE VIEUX<br>COUSIN</div>

  <div class="venue-mark">
    <span class="venue-dot"></span>
    <span class="venue-name">LE CINQUANTE SEPT</span>
  </div>
  <div class="venue-tag venue-tag--left">BAR BRASSERIE</div>
  <div class="venue-tag venue-tag--right">COCKTAILS - BIÈRE - CHAMPAGNE - VINS</div>

  <div class="event-place">57 à CAMBRAI</div>
  <div class="event-welcome">ACCUEIL !</div>
  <div class="event-when event-when--date">VENDREDI<span>MAI 13, 2022</span></div>
  <div class="event-divider"></div>
  <div class="event-when event-when--time">A PARTIR DE<span>19 H</span></div>
  <div class="event-program">AU PROGRAMME,<span>SÉANCE PHOTO ET DÉDICACES.</span></div>

  <div class="vip">
    <div class="vip-frame"></div>
    <div class="vip-content">
      <div class="vip-price">€65</div>
      <div class="vip-label">TABLE VIP</div>
      <div class="vip-offer">SERA OFFERTE<br>POUR<br>PARTAGER LE REPAS<br>AVEC LUI!</div>
      <div class="vip-menu">(ENTRÉE - PLAT - DESSERT) ; CHAMPAGNE.</div>
      <div class="vip-seats">SEULEMENT 12 PLACES<span>DISPONIBLE À SA TABLE !</span></div>
    </div>
  </div>

  <div class="extras-bbq">La brasserie vous proposera<br>un barbecue pour l'occasion.</div>
  <div class="extras-price">€15</div>
  <div class="extras-note extras-note--admission">Admission<br>avec repas</div>
  <div class="extras-divider"></div>
  <svg class="extras-icon" viewBox="0 0 48 52" aria-hidden="true">
    <g fill="none" stroke="#fff" stroke-width="4" stroke-linecap="round">
      <circle cx="24" cy="28" r="17"/>
      <path d="M24 19v10l6 4"/>
      <path d="M14 49l4-5M34 49l-4-5"/>
    </g>
    <path d="M3 14a9 9 0 0 1 12-10z M45 14a9 9 0 0 0-12-10z" fill="#fff"/>
  </svg>
  <div class="extras-note extras-note--happy">sur les bières<br>et les cocktails !</div>

  <div class="footer-band-left"></div>
  <div class="footer-band-right"></div>
  <div class="footer-note">*Réservation fortement conseillée.</div>
</div>
</body>
</html>
```